Brightline Power Crew, LLC New Business Card Design Project

Please do not submit multiple designs that look similar. Many submittals of nearly the same design will result in auto rejection. Please do not submit a design unless you know how to provide a PDF with recognizable text that I can modify and update using Adobe Acrobat. I do not use Adobe Photoshop. Please design a business card using the attached BPC logo. Be creative. Do at least 2-3 different designs. One side should have the logo large with the URL www.BPC-RT.com. The other side of the card should have the name Marcus Pellham. License number 524318. Phone number 860-555-0147. Email service@BPC-RT.com. Physical address 742 Fenwick Orchard Road, Suite 5, Harlow Bend, VT. 06981. The company name should also be spelled out somewhere, Brightline Power Crew, LLC. Please ensure there is no tiny font. Please also ensure that there is nothing near the edges that might get cut off during printing. It will be 3.5" x 2" horizontal standard business card. I use CardMintly.com to order. The customer has said they want the business card to use the attached look and color scheme. Please do not submit a design unless you know how to provide a PDF with recognizable text that I can modify and update using Adobe Acrobat. I do not use Adobe Photoshop.
Target Market(s)
Read all instructions above.
Industry/Entity Type
Contact Information for Business Card
Requirements
Must have
- Read all instructions above.
Nice to have
Should not have

```html
<!DOCTYPE html>
<html lang="en">
<head>
<meta charset="utf-8">
<title>Brightline Power Crew, LLC – Business Card</title>
<link rel="stylesheet" href="https://fonts.googleapis.com/css2?family=Marcellus&display=swap">
<style>
  :root {
    --ink: #1f1d1e;
    --ribbon: #3b3b3d;
    --paper: #ffffff;
    --paper-shade: #ececec;
    --stage: #d9d9da;
    --soft-text: #e6e6e6;
  }
  * { box-sizing: border-box; margin: 0; padding: 0; }
  html, body { width: 1200px; height: 900px; overflow: hidden; }
  body {
    background: var(--stage);
    font-family: "Marcellus", serif;
    color: var(--ink);
    position: relative;
  }
  .card {
    position: absolute;
    left: 285px;
    width: 630px;
    height: 360px;
    background: linear-gradient(135deg, var(--paper) 0%, var(--paper) 60%, var(--paper-shade) 100%);
    box-shadow: 0 6px 18px rgba(0,0,0,.18);
    overflow: hidden;
  }
  .card-front { top: 50px; }
  .card-back { top: 480px; }

  /* Front */
  .front-band {
    position: absolute; top: 0; right: 0; width: 78px; height: 100%;
    background: var(--ink);
  }
  .front-rule {
    position: absolute; top: 0; right: 88px; width: 4px; height: 100%;
    background: var(--ink);
  }
  .brand-block {
    position: absolute; left: 60px; top: 0; width: 410px; height: 100%;
    display: flex; flex-direction: column; align-items: center; justify-content: center;
    text-align: center;
  }
  .brand-mark { display: flex; align-items: center; gap: 16px; }
  .brand-dot { width: 46px; height: 46px; border-radius: 50%; background: var(--ink); }
  .brand-initials { font-size: 72px; line-height: 1; letter-spacing: 2px; }
  .brand-name { margin-top: 18px; font-size: 24px; }
  .brand-url { margin-top: 10px; font-size: 26px; letter-spacing: .5px; }

  /* Back */
  .back-dark {
    position: absolute; top: 0; left: 0; width: 352px; height: 100%;
    background: var(--ink);
  }
  .back-rule {
    position: absolute; top: 0; left: 362px; width: 3px; height: 100%;
    background: var(--ink);
  }
  .name-ribbon {
    position: absolute; left: 0; top: 84px; width: 352px; height: 62px;
    background: var(--ribbon);
    display: flex; align-items: center; padding-left: 40px;
  }
  .name-ribbon::after {
    content: ""; position: absolute; right: -22px; top: 0;
    border-left: 22px solid var(--ribbon);
    border-top: 31px solid transparent; border-bottom: 31px solid transparent;
  }
  .person-name { font-size: 28px; font-weight: 400; color: var(--soft-text); }
  .contact {
    position: absolute; left: 40px; color: var(--soft-text);
    display: flex; align-items: flex-start; gap: 12px; font-size: 19px; line-height: 1.35;
  }
  .contact svg { flex: none; margin-top: 3px; }
  .contact-phone { top: 172px; }
  .contact-email { top: 262px; }
  .contact-address { top: 292px; }
  .back-mark {
    position: absolute; right: 60px; top: 48px;
    display: flex; align-items: center; gap: 14px;
  }
  .back-mark .brand-dot { width: 36px; height: 36px; }
  .back-mark .brand-initials { font-size: 58px; }
  .license {
    position: absolute; right: 36px; bottom: 34px; font-size: 17px;
  }
</style>
</head>
<body>

<section class="card card-front" aria-label="Business card front">
  <div class="brand-block">
    <div class="brand-mark">
      <span class="brand-dot"></span>
      <span class="brand-initials">BPC</span>
    </div>
    <p class="brand-name">Brightline Power Crew, LLC</p>
    <p class="brand-url">www.BPC-RT.com</p>
  </div>
  <div class="front-rule"></div>
  <div class="front-band"></div>
</section>

<section class="card card-back" aria-label="Business card back">
  <div class="back-dark"></div>
  <div class="back-rule"></div>
  <div class="name-ribbon"><h1 class="person-name">Marcus Pellham</h1></div>

  <p class="contact contact-phone">
    <svg width="12" height="20" viewBox="0 0 12 20" aria-hidden="true"><rect x="1" y="1" width="10" height="18" rx="2" fill="none" stroke="currentColor" stroke-width="1.5"/><line x1="4.5" y1="16" x2="7.5" y2="16" stroke="currentColor" stroke-width="1.5"/></svg>
    860-555-0147
  </p>
  <p class="contact contact-email">
    <svg width="18" height="14" viewBox="0 0 18 14" aria-hidden="true"><rect x="1" y="1" width="16" height="12" rx="2" fill="currentColor"/><path d="M2 2 L9 8 L16 2" fill="none" stroke="#1f1d1e" stroke-width="1.5"/></svg>
    service@BPC-RT.com
  </p>
  <p class="contact contact-address">
    <svg width="16" height="20" viewBox="0 0 16 20" aria-hidden="true"><path d="M8 1 C4 1 1.5 4 1.5 7.5 C1.5 12 8 19 8 19 C8 19 14.5 12 14.5 7.5 C14.5 4 12 1 8 1 Z" fill="none" stroke="currentColor" stroke-width="1.6"/><circle cx="8" cy="7.5" r="2.3" fill="currentColor"/></svg>
    <span>742 Fenwick Orchard Road<br>Suite 5, Harlow Bend, VT. 06981</span>
  </p>

  <div class="back-mark">
    <span class="brand-dot"></span>
    <span class="brand-initials">BPC</span>
  </div>
  <p class="license">License number 524318</p>
</section>

</body>
</html>
```